Psychologist website

Simple psychologist website
Site map:
home
self-test
common conditions
children
contact
about
info

Current website:
http://www.moriklepsychology.com.au/

Not in love with logo, or colours etc - open brief
Happy for new font/style/logo for company name

Customer wants clean, credible and warm and friendly look & feel
stock photos OK

Brief:

One home page - simple with 2 or 3 small areas to tease and attract the user and one template page to suit all the other pages

Pages structurally similar to
http://www.quellbyhouse.com.au/
In that the home page is different and the other pages are based on one template

Requirements
Must have
• 2 pages - one home page and one template page
• navigation for site map

```html
<!DOCTYPE html>
<html lang="en">
<head>
<meta charset="utf-8">
<title>Morikle &amp; Associates – Clinical Psychologists</title>
<link rel="stylesheet" href="https://fonts.googleapis.com/css2?family=Montserrat:wght@400;500;600;700&family=Playfair+Display:ital,wght@0,400;0,700;1,400&family=Alfa+Slab+One&family=Kalam:wght@400&display=swap">
<style>
  :root{
    --green:#3a8a3c;
    --leaf:#3f9440;
    --mint:#6fcf8c;
    --gold:#f4c21f;
    --orange:#f39a1d;
    --rose:#c4566a;
    --sage:#6aa55a;
    --ink:#1f1f1f;
    --text:#555;
    --grey-band:#f0eeee;
    --nav-bg:#f2f2f2;
    --frame:#d6d6d6;
  }
  *{box-sizing:border-box;margin:0;padding:0}
  html,body{width:1017px;height:1200px;overflow:hidden;background:#fff}
  body{font-family:"Montserrat",sans-serif;color:var(--text);position:relative}
  .page{position:relative;width:1017px;height:1200px;overflow:hidden}

  /* header */
  .brand{position:absolute;left:120px;top:18px;display:flex;flex-direction:column;gap:8px}
  .brand-name{font-weight:700;font-size:26px;letter-spacing:-0.3px;color:var(--green);line-height:1}
  .brand-tag{font-size:11px;letter-spacing:7px;color:#666;font-weight:500;line-height:1}
  .header-contact{position:absolute;left:692px;top:18px;display:flex;gap:10px;align-items:center}
  .header-contact .label{font-family:"Kalam",cursive;font-size:12px;color:#666;line-height:1}
  .header-contact .number{font-family:"Alfa Slab One",serif;font-size:22px;color:#222;letter-spacing:1px;line-height:1.1}

  .nav{position:absolute;left:0;top:82px;width:100%;height:35px;background:linear-gradient(#fdfdfd,var(--nav-bg));border-bottom:3px solid var(--green)}
  .nav ul{list-style:none}
  .nav li{position:absolute;top:10px;font-weight:600;font-size:13px;color:var(--ink);white-space:nowrap;line-height:1.2}

  /* hero */
  .hero{position:absolute;left:0;top:120px;width:1017px;height:440px}
  .hero-photo{position:absolute;inset:0 0 40px 0;background:
    linear-gradient(180deg,#cfcbae 0%,#b9bb8c 30%,#9aab68 60%,#a9ab55 85%,#c4b95e 100%)}
  .hero svg{position:absolute;left:0;top:0}
  .hero-title{position:absolute;left:122px;top:124px;font-family:"Playfair Display",serif;font-weight:400;font-size:27.5px;color:#fff;line-height:1.32}
  .hero-more{position:absolute;left:128px;top:218px;font-family:"Playfair Display",serif;font-weight:700;font-size:15.5px;color:#fff;text-decoration:underline}
  .hero-dots{position:absolute;left:222px;top:285px;display:flex;gap:11px}
  .hero-dots span{width:11px;height:11px;border-radius:50%;background:#fff}
  .hero-dots span.active{background:var(--gold)}
  .treat{position:absolute;left:120px;top:346px;font-size:28px;color:var(--ink);font-weight:400;letter-spacing:-0.5px;white-space:nowrap}
  .treat strong{font-weight:700}
  .cond{position:absolute;font-family:"Playfair Display",serif;color:#fff;font-size:21px;line-height:1.15}

  /* teasers */
  .teasers{position:absolute;left:119px;top:582px;display:flex;gap:23px}
  .teaser{width:244px;text-align:center}
  .teaser h2{font-family:"Playfair Display",serif;font-weight:400;font-size:19px;color:var(--ink);margin-bottom:8px;line-height:1.2}
  .teaser .photo{height:119px;border:5px solid var(--frame)}
  .teaser p{font-size:10.6px;line-height:17.4px;color:#555;margin:14px 2px 0}
  .btn{display:inline-block;margin-top:17px;background:var(--mint);color:#fff;font-family:"Playfair Display",serif;font-weight:700;font-size:10px;text-decoration:underline;padding:4px 12px;border-radius:3px}

  /* intro band */
  .intro{position:absolute;left:0;top:893px;width:100%;height:130px;background:var(--grey-band);padding:20px 150px 0}
  .intro p{font-style:italic;font-size:12.4px;line-height:22px;color:#666;text-align:center}
  .intro a{font-size:8.5px;font-weight:700;color:#333;text-decoration:none}

  /* footer */
  .footer{position:absolute;left:0;top:1078px;width:100%;height:122px;background:var(--green)}
  .footer svg{position:absolute;left:0;top:-10px}
  .footer .label{position:absolute;left:125px;top:36px;font-family:"Kalam",cursive;font-size:12px;color:#fff}
  .footer .number{position:absolute;left:120px;top:50px;font-family:"Alfa Slab One",serif;font-size:29px;color:var(--gold);letter-spacing:1px;line-height:1.2}
  .footer-nav{position:absolute;left:498px;top:39px;font-size:10px;color:#fff;font-weight:500;white-space:nowrap}
  .copyright{position:absolute;left:498px;top:67px;font-size:10px;color:#fff;font-weight:500}
</style>
</head>
<body>
<div class="page">

  <header>
    <div class="brand">
      <span class="brand-name">MORIKLE &amp; ASSOCIATES</span>
      <span class="brand-tag">CLINICAL PSYCHOLOGISTS</span>
    </div>
    <div class="header-contact">
      <svg width="38" height="40" viewBox="0 0 38 40" aria-hidden="true">
        <rect x="10" y="2" width="26" height="34" rx="5" fill="var(--orange)"/>
        <rect x="14" y="6" width="18" height="8" rx="1" fill="#fff"/>
        <g fill="#fff"><circle cx="17" cy="19" r="1.6"/><circle cx="23" cy="19" r="1.6"/><circle cx="29" cy="19" r="1.6"/><circle cx="17" cy="25" r="1.6"/><circle cx="23" cy="25" r="1.6"/><circle cx="29" cy="25" r="1.6"/><circle cx="17" cy="31" r="1.6"/><circle cx="23" cy="31" r="1.6"/><circle cx="29" cy="31" r="1.6"/></g>
        <path d="M8 4 C2 4 2 36 8 38" stroke="var(--orange)" stroke-width="4" fill="none" stroke-linecap="round"/>
      </svg>
      <div>
        <div class="label">For all appointments &amp; enquiries</div>
        <div class="number">95550142</div>
      </div>
    </div>
  </header>

  <nav class="nav">
    <ul>
      <li style="left:129px">HOME</li>
      <li style="left:214px">SELF TEST</li>
      <li style="left:327px">COMMON CONDITIONS</li>
      <li style="left:522px">CHILDREN</li>
      <li style="left:633px">CONTACT</li>
      <li style="left:742px">ABOUT US</li>
      <li style="left:855px">INFO</li>
    </ul>
  </nav>

  <section class="hero">
    <div class="hero-photo" role="img" aria-label="Photo of a young woman lying in a meadow of wildflowers"></div>
    <svg width="1017" height="440" viewBox="0 0 1017 440" aria-hidden="true">
      <defs>
        <linearGradient id="sand" x1="0" y1="0" x2="0" y2="1">
          <stop offset="0" stop-color="#e9dcc0"/>
          <stop offset="0.35" stop-color="#fff"/>
        </linearGradient>
      </defs>
      <path d="M0 340 C120 290 250 265 360 272 C520 282 700 370 1017 392 L1017 440 L0 440 Z" fill="url(#sand)"/>
      <path d="M46 180 C110 100 250 70 380 82 C450 88 500 108 530 116 C500 190 430 300 330 320 C230 340 120 300 46 180 Z" fill="var(--leaf)" opacity="0.93"/>
      <path d="M600 330 C640 300 700 300 760 345 C730 390 680 410 640 400 C615 390 600 360 600 330 Z" fill="var(--rose)" opacity="0.88"/>
      <path d="M698 295 C740 255 820 245 880 250 C870 310 820 350 745 355 C720 340 705 320 698 295 Z" fill="var(--orange)" opacity="0.9"/>
      <path d="M745 375 C770 340 840 335 905 345 C880 410 830 435 780 430 C760 415 748 395 745 375 Z" fill="var(--sage)" opacity="0.9"/>
    </svg>
    <h1 class="hero-title">Psychologists, in Sydney,<br>Chatswood, and Westmead.</h1>
    <span class="hero-more">Read more...</span>
    <div class="hero-dots"><span class="active"></span><span></span><span></span><span></span><span></span></div>
    <p class="treat">We provide <strong>expert treatment</strong> for</p>
    <span class="cond" style="left:736px;top:296px">depression</span>
    <span class="cond" style="left:641px;top:340px">anxiety</span>
    <span class="cond" style="left:777px;top:358px">eating<br>disorders</span>
  </section>

  <section class="teasers">
    <article class="teaser">
      <h2>Self Test</h2>
      <div class="photo" role="img" aria-label="Photo of a thoughtful young woman in a dark hoodie against a grey sky" style="background:linear-gradient(160deg,#d9dde0,#8b8f93 60%,#2c2d30)"></div>
      <p>Lorem Ipsum is simply dummy text of the printing and typesetting industry. Lorem Ipsum has been the industry's standard dummy text ever since the 1500s.</p>
      <span class="btn">Read more...</span>
    </article>
    <article class="teaser">
      <h2>Common Conditions</h2>
      <div class="photo" role="img" aria-label="Photo of a man talking with a therapist in a bright clinic" style="background:linear-gradient(100deg,#f2f4f6,#cfdde8 45%,#e7d2c0 65%,#c8dbe8)"></div>
      <p>Lorem Ipsum is simply dummy text of the printing and typesetting industry. Lorem Ipsum has been the industry's standard dummy text ever since the 1500s.</p>
      <span class="btn">Read more...</span>
    </article>
    <article class="teaser">
      <h2>Children</h2>
      <div class="photo" role="img" aria-label="Photo of a young boy holding his head with both hands" style="background:linear-gradient(120deg,#c9a77a,#e8cfb0 50%,#d8b58a)"></div>
      <p>Lorem Ipsum is simply dummy text of the printing and typesetting industry. Lorem Ipsum has been the industry's standard dummy text ever since the 1500s.</p>
      <span class="btn">Read more...</span>
    </article>
  </section>

  <section class="intro">
    <p>Our psychologists provide a comfortable, supportive, and confidential environment for their clients. Our first goal is for you to feel comfortable in exploring issues and sharing sharing your concerns, knowing that you have been heard and understood. It is in this kind of environment that client and therapist can work productively to understand problems and seek solutions. <a>[Read More...]</a></p>
  </section>

  <footer class="footer">
    <svg width="1017" height="14" viewBox="0 0 1017 14" preserveAspectRatio="none" aria-hidden="true">
      <path d="M0 14 L0 6 L40 4 L90 7 L150 3 L210 6 L280 2 L340 6 L400 4 L470 7 L540 3 L600 6 L660 4 L730 7 L790 3 L850 6 L920 4 L970 6 L1017 3 L1017 14 Z" fill="var(--green)"/>
    </svg>
    <span class="label">For all appointments &amp; enquiries</span>
    <span class="number">95550142</span>
    <div class="footer-nav">Home&nbsp; / &nbsp;Self Test&nbsp; / &nbsp;Common Conditions&nbsp; / &nbsp;Children&nbsp; / Contact&nbsp; / &nbsp;About Us&nbsp; / &nbsp;Info</div>
    <div class="copyright">Copyright © 2013 Morikle Psychology. All Rights Reserved.</div>
  </footer>

</div>
</body>
</html>
```